Psychology and personal development service needs an awesome Web Design

Hi, we are Bright, Steady & Kind, a psychology and personal development service located in Melbourne Australia. We already have a website www.brightsteady&kind.org but it is in great need of a makeover! We add to the website regularly with articles and so we need a space to archive these when they come off the main page, and we have products that we would like to sell internationally so we need a shop page that can convert currencies for international sales and calculate postage and handling. We have a Facebook page that we would like to link as well as a newsletter that we would like to archive on the website. We have just had a logo designed through craft huddle and would like to incorporate this into our website. We want something with high visual impact and uncluttered.
We also run workshops and events so need a tab for this.
Thanks for getting on board!

```html
<!DOCTYPE html>
<html lang="en">
<head>
<meta charset="utf-8">
<title>Bright, Steady &amp; Kind</title>
<link rel="stylesheet" href="https://fonts.googleapis.com/css2?family=Bodoni+Moda:wght@400;500;600&family=EB+Garamond:wght@400&display=swap">
<style>
  :root {
    --page-bg: #e8e9ed;
    --panel-bg: #ffffff;
    --nav-bg: #37b8a2;
    --nav-active: #4fa894;
    --nav-text: #ffffff;
    --brand-purple: #7a5c9a;
    --heading-purple: #6b4aa0;
    --accent-pink: #e0559a;
    --button-blue: #48a7d9;
    --body-text: #1e1e1e;
    --topic-text: #666666;
    --footer-text: #999999;
    --cover-dark: #2f2620;
    --cover-light: #6b5a48;
  }
  * { margin: 0; padding: 0; box-sizing: border-box; }
  html, body { width: 800px; height: 1200px; overflow: hidden; }
  body {
    background: var(--page-bg);
    font-family: "EB Garamond", Georgia, serif;
    color: var(--body-text);
    position: relative;
  }
  .site-header {
    position: absolute; left: 0; top: 22px; width: 800px; height: 142px;
    display: flex; align-items: center; justify-content: center; gap: 16px;
  }
  .brand-dot { width: 44px; height: 44px; border-radius: 50%; background: var(--brand-purple); }
  .brand-name {
    font-family: "Bodoni Moda", Georgia, serif; font-weight: 400;
    font-size: 38px; color: var(--brand-purple); letter-spacing: 1px;
  }
  .main-nav {
    position: absolute; left: 80px; top: 241px; width: 640px; height: 52px;
    background: var(--nav-bg); display: flex;
  }
  .main-nav a {
    display: flex; align-items: center; justify-content: center;
    color: var(--nav-text); text-decoration: none;
    font-family: "Bodoni Moda", Georgia, serif; font-size: 20px; letter-spacing: 0.5px;
  }
  .main-nav a.is-active { background: var(--nav-active); }
  .panel { position: absolute; left: 80px; width: 640px; background: var(--panel-bg); }
  .panel-heading {
    font-family: "Bodoni Moda", Georgia, serif; font-weight: 600;
    font-size: 19px; color: var(--heading-purple); text-align: center;
  }
  .welcome { top: 318px; height: 176px; }
  .welcome .panel-heading { position: absolute; top: 29px; width: 100%; }
  .welcome p {
    position: absolute; top: 78px; left: 55px; width: 530px;
    text-align: center; font-size: 14px; line-height: 19.3px;
  }
  .book-feature { top: 516px; height: 239px; }
  .book-cover {
    position: absolute; left: 13px; top: 13px; width: 143px; height: 214px;
    background: linear-gradient(160deg, var(--cover-light), var(--cover-dark));
  }
  .book-tag {
    position: absolute; left: 173px; top: 17px;
    font-size: 14px; color: var(--accent-pink);
  }
  .book-title {
    position: absolute; left: 173px; top: 40px;
    font-family: "Bodoni Moda", Georgia, serif; font-weight: 400; font-size: 19px;
  }
  .book-blurb {
    position: absolute; left: 173px; top: 74px; width: 446px;
    font-size: 10.3px; line-height: 15.6px;
  }
  .button {
    position: absolute; top: 179px; height: 48px;
    display: flex; align-items: center; justify-content: center;
    background: var(--button-blue); color: #fff; text-decoration: none;
    font-family: "Bodoni Moda", Georgia, serif; font-weight: 500; font-size: 19px;
  }
  .button-read { left: 326px; width: 143px; }
  .button-shop { left: 480px; width: 149px; }
  .topics { top: 778px; height: 325px; }
  .topics .panel-heading { position: absolute; top: 33px; width: 100%; }
  .topic {
    position: absolute; width: 160px; margin-left: -80px; text-align: center;
    font-size: 13.8px; color: var(--topic-text);
  }
  .site-footer {
    position: absolute; left: 81px; top: 1138px;
    font-size: 11px; color: var(--footer-text);
  }
</style>
</head>
<body>
  <header class="site-header">
    <span class="brand-dot"></span>
    <span class="brand-name">Bright, Steady &amp; Kind</span>
  </header>

  <nav class="main-nav">
    <a class="is-active" href="#" style="width:102px">Home</a>
    <a href="#" style="width:136px">Shop</a>
    <a href="#" style="width:88px">Blog</a>
    <a href="#" style="width:188px">Workshops</a>
    <a href="#" style="width:126px">Contact</a>
  </nav>

  <section class="panel welcome">
    <h1 class="panel-heading">Hello and welcome!</h1>
    <p>We are a psychology and personal development service located in Melbourne Australia. Phasellus vel velit tincidunt, tempor leo a, ornare turpis. Nullam non lorem massa. Phasellus at metus et orci gravida eleifend.</p>
  </section>

  <section class="panel book-feature">
    <div class="book-cover" role="img" aria-label="Book cover for Wren: My Mother Kept Bees by Hanna Morrow"></div>
    <p class="book-tag">New book in the shop!</p>
    <h2 class="book-title">Wren: My Mother Kept Bees</h2>
    <p class="book-blurb">Seventeen-year-old Wren is on a search for identity and transformation as she attempts to come to terms with the death of her mother: a beekeeper—her hero—and light of her life. Wren, who has already lived a challenging existence, is anxious to make sense of her life.</p>
    <a class="button button-read" href="#">Read more</a>
    <a class="button button-shop" href="#">View in Shop</a>
  </section>

  <section class="panel topics">
    <h2 class="panel-heading">Lets talk about...</h2>
    <span class="topic" style="left:81px;top:89px">Body talk</span>
    <span class="topic" style="left:220px;top:89px">Relationships</span>
    <span class="topic" style="left:390px;top:89px">Parents &amp; children</span>
    <span class="topic" style="left:555px;top:89px">Technology</span>
    <span class="topic" style="left:82px;top:170px">Surfing</span>
    <span class="topic" style="left:221px;top:170px">Transforming</span>
    <span class="topic" style="left:391px;top:170px">Discover self worth</span>
    <span class="topic" style="left:555px;top:170px">Success</span>
    <span class="topic" style="left:83px;top:253px">Parasites</span>
    <span class="topic" style="left:223px;top:253px">Creating a legacy</span>
    <span class="topic" style="left:397px;top:253px">I don't have time</span>
    <span class="topic" style="left:558px;top:253px">Miscellaneous</span>
  </section>

  <footer class="site-footer">Copyright 2014 © Bright, Steady &amp; Kind</footer>
</body>
</html>
```